Flyer-Design für Immobilienfirma
Zielgruppe
www.brenkholt-immobilien.de
Aufgabenstellung
Thema :
Neukunden generieren – Viele Wege führen zu neuen Leads ...
Sich selbst als Experten platzieren mit Bild
Dienstleistung : FÜR DEN IMMOBILIENBESITZER
Was ist Ihre Immobilie wert?
KOSTENLOSE Beratung durch Experten
KOSTENLOSE Immobilienbewertung
KOSTENLOS vorhandene Grundrisszeichnungen aktualisieren
KOSTENLOS 3D Grundrisszeichnungen und Ansicht
KOSTENLOS 3D Fotos und 360 Grad Ansichten
KOSTENLOS Drohnenaufnahmen IHRER Immobilien
KOSTENLOS Erstellung eines Energieverbrauchsausweises
evtl für die Rückseite
#Tippgeberprämie
Brenkholt & Partner Immobilien
so einfach verdienen Sie sich Ihre Tippprämie
wenn Sie Kenntnis vom beabsichtigten Verkauf einer Immobilie haben, dann setzen Sie sich mit uns in Verbindung.
Wir belohnen Ihren Tipp – wenn er zu einem Verkaufsabschluss durch uns führt –
mit 10 Prozent der an uns gezahlten Netto-Vermittlungsprovision (ohne MwSt.).
Dies gilt auch für Eigentümer, die uns Ihre Immobilie zum Verkauf geben.
Voraussetzungen für die Zahlung einer Tippgeber-Prämie sind:
Die Brenkholt & Partner immobilien kennt das angebotene Objekt noch nicht.
Das Objekt wird nicht bereits im Internet von dritter Seite beworben.
Die Brenkholt & Partner immobilien erhält die Erlaubnis zur Vermarktung der Immobilie.
Es kommt zu einem durch die Brenkholt & Partner immobilien vermittelten Verkauf
Sie erhalten Ihre Tippprämie unmittelbar nach Zahlung der Courtage an uns auf ein von Ihnen genanntes Konto überwiesen!

```html
<!DOCTYPE html>
<html lang="de">
<head>
<meta charset="utf-8">
<title>Brenkholt & Partner – Flyer</title>
<link rel="stylesheet" href="https://fonts.googleapis.com/css2?family=Montserrat:wght@300;400;500;600;700;800&display=swap">
<style>
  :root{
    --brown:#3b3127;
    --brown-soft:#4a3f33;
    --gold:#c99a3b;
    --gold-light:#e0b55a;
    --white:#ffffff;
    --ink:#3a3530;
    --bg:#d7d7d9;
  }
  *{box-sizing:border-box;margin:0;padding:0}
  html,body{width:1200px;height:2400px;overflow:hidden}
  body{background:var(--bg);font-family:"Montserrat",sans-serif;color:var(--ink);position:relative}
  .flyer{position:absolute;left:190px;width:820px;height:1160px;background:var(--white);overflow:hidden;box-shadow:0 10px 30px rgba(0,0,0,.18)}
  .flyer--front{top:30px}
  .flyer--back{top:1210px}
  .layer{position:absolute;inset:0;width:820px;height:1160px}

  /* front top */
  .brand-column{position:absolute;left:0;top:0;width:340px;height:560px;background:var(--brown)}
  .portrait{position:absolute;left:340px;top:0;width:480px;height:580px;
    background:linear-gradient(160deg,#e9e2d6 0%,#c7ab86 35%,#8f97ab 62%,#2c3b5a 100%)}
  .brand{position:absolute;left:60px;top:70px;display:flex;align-items:center;gap:12px;color:var(--white);font-weight:600;font-size:30px;letter-spacing:.5px}
  .brand__mark{width:14px;height:14px;background:var(--gold)}
  .tagline{position:absolute;left:60px;top:150px;width:220px;padding:22px 10px;border:2px solid var(--gold);color:var(--white);
    text-align:center;font-weight:500;font-size:20px;line-height:1.2;text-transform:uppercase}
  .url-band{position:absolute;left:60px;top:290px;width:220px;padding:7px 0;background:var(--gold);color:var(--white);text-align:center;font-size:12px;font-weight:600}
  .name-badge{position:absolute;right:0;top:420px;width:250px}
  .name-badge__name{background:var(--gold);color:var(--white);font-weight:600;font-size:20px;padding:8px 18px}
  .name-badge__role{background:var(--brown);color:var(--white);font-weight:500;font-size:18px;padding:8px 18px}

  .headline{position:absolute;left:0;width:820px;top:590px;text-align:center}
  .headline__title{font-weight:800;font-size:38px;color:var(--brown);text-transform:uppercase;letter-spacing:.5px}
  .headline__sub{margin-top:6px;font-size:22px;font-weight:400;color:var(--gold);text-transform:uppercase;letter-spacing:1px}
  .headline__sub::before,.headline__sub::after{content:"";display:inline-block;width:60px;height:2px;background:var(--gold);vertical-align:middle;margin:0 14px}

  .services{position:absolute;top:700px;left:60px;right:50px;display:grid;grid-template-columns:1fr 1fr;column-gap:60px}
  .services__col{display:flex;flex-direction:column;gap:26px}
  .services__col + .services__col{padding-left:40px;border-left:1px solid #cfc8bd}
  .service{display:flex;align-items:center;gap:18px}
  .service__icon{flex:none;width:62px;height:62px;border-radius:50%;border:3px solid var(--gold);display:flex;align-items:center;justify-content:center;background:var(--white)}
  .service__label{font-weight:700;color:var(--gold);font-size:16px;text-transform:uppercase}
  .service__text{font-size:17px;line-height:1.2;color:var(--ink)}

  /* footer */
  .contact{position:absolute;color:var(--white);font-size:12px;line-height:1.35;display:flex;gap:8px}
  .contact__icon{flex:none;width:20px;height:20px;border:1.5px solid var(--white);border-radius:50%;display:flex;align-items:center;justify-content:center}
  .contact strong{font-weight:600}
  .contact--address{left:40px;top:1020px}
  .contact--phone{left:300px;top:1045px}
  .contact--mail{left:560px;top:1075px}
  .contact-url{position:absolute;left:328px;top:1095px;color:var(--white);font-size:12px;font-weight:600}

  /* back */
  .street{position:absolute;left:0;top:0;width:820px;height:520px;
    background:linear-gradient(180deg,#b9d0e6 0%,#8fa36a 30%,#6c5a48 65%,#c9b39a 100%)}
  .hotline{position:absolute;right:40px;top:115px;display:flex}
  .hotline__icon{width:60px;height:60px;background:var(--brown);display:flex;align-items:center;justify-content:center}
  .hotline__text{background:var(--gold);color:var(--white);padding:8px 18px}
  .hotline__label{font-size:14px;font-weight:400}
  .hotline__number{font-size:24px;font-weight:700;letter-spacing:.5px}
  .tip-title{position:absolute;left:0;width:820px;top:440px;text-align:center}
  .tip-title__main{color:var(--white);font-weight:800;font-size:44px;letter-spacing:1px}
  .tip-title__sub{color:var(--gold);font-size:17px;letter-spacing:1.5px;text-transform:uppercase;margin-top:4px}
  .tip-title__sub::before,.tip-title__sub::after{content:"";display:inline-block;width:40px;height:2px;background:var(--gold);vertical-align:middle;margin:0 12px}
  .tip-body{position:absolute;left:70px;right:70px;top:640px;font-size:15px;line-height:1.45;color:var(--ink)}
  .tip-body p{margin-bottom:10px}
  .tip-body strong{font-weight:700;color:var(--brown)}
  .conditions{list-style:none;margin-bottom:10px}
  .conditions li{position:relative;padding-left:24px}
  .conditions li::before{content:"";position:absolute;left:0;top:5px;width:12px;height:12px;border-radius:50%;background:var(--gold)}
</style>
</head>
<body>

<!-- Front side -->
<section class="flyer flyer--front">
  <div class="brand-column"></div>
  <div class="portrait" role="img" aria-label="Porträtfoto des Geschäftsführers im blauen Sakko"></div>

  <div class="brand"><span class="brand__mark"></span>Brenkholt &amp; Partner</div>
  <div class="tagline">Service.<br>Qualität.<br>Flexibilität.</div>
  <div class="url-band">www.brenkholt-immobilien.de</div>

  <div class="name-badge">
    <div class="name-badge__name">Henrik Brenkholt</div>
    <div class="name-badge__role">Geschäftsführer</div>
  </div>

  <svg class="layer" viewBox="0 0 820 1160" aria-hidden="true">
    <path d="M0,505 Q420,500 820,600 L820,612 Q420,514 0,520 Z" fill="#c99a3b"/>
    <path d="M0,520 Q420,514 820,612 L820,1160 L0,1160 Z" fill="#ffffff"/>
    <path d="M0,960 C320,965 600,1010 820,1085" fill="none" stroke="#c99a3b" stroke-width="5"/>
    <path d="M0,975 C320,980 600,1025 820,1100 L820,1160 L0,1160 Z" fill="#3b3127"/>
  </svg>

  <div class="headline">
    <div class="headline__title">Was ist Ihre Immobilie wert?</div>
    <div class="headline__sub">Unser Service für Sie</div>
  </div>

  <div class="services">
    <div class="services__col">
      <div class="service">
        <div class="service__icon"><svg width="30" height="28" viewBox="0 0 30 28"><path d="M3,3 H27 V19 H12 L6,25 V19 H3 Z" fill="#3b3127"/></svg></div>
        <div><div class="service__label">Kostenlose</div><div class="service__text">Beratung durch<br>Experten</div></div>
      </div>
      <div class="service">
        <div class="service__icon"><svg width="30" height="28" viewBox="0 0 30 28"><rect x="2" y="12" width="6" height="14" fill="#3b3127"/><path d="M10,12 L16,2 Q19,2 18,8 L17,11 H26 Q28,12 27,15 L24,25 Q23,26 21,26 H10 Z" fill="#3b3127"/></svg></div>
        <div><div class="service__label">Kostenlose</div><div class="service__text">Immobilien-<br>bewertung</div></div>
      </div>
      <div class="service">
        <div class="service__icon"><svg width="30" height="30" viewBox="0 0 30 30" fill="none" stroke="#3b3127" stroke-width="3.5"><path d="M5,14 A10,10 0 0 1 23,8"/><path d="M25,16 A10,10 0 0 1 7,22"/><path d="M18,7 H24 V1" stroke-width="3"/><path d="M12,23 H6 V29" stroke-width="3"/></svg></div>
        <div><div class="service__label">Kostenlos</div><div class="service__text">vorhandene Grund-<br>zeichnung aktualisieren</div></div>
      </div>
    </div>
    <div class="services__col">
      <div class="service">
        <div class="service__icon"><svg width="30" height="26" viewBox="0 0 30 26"><rect x="2" y="3" width="26" height="20" fill="none" stroke="#3b3127" stroke-width="3"/><path d="M5,20 L12,11 L17,16 L21,12 L25,20 Z" fill="#c99a3b"/><circle cx="21" cy="8" r="2.5" fill="#3b3127"/></svg></div>
        <div><div class="service__label">Kostenlose</div><div class="service__text">3D Grundzeichnung,<br>3D Fotos</div></div>
      </div>
      <div class="service">
        <div class="service__icon"><svg width="24" height="30" viewBox="0 0 24 30"><path d="M2,2 H16 L22,8 V28 H2 Z" fill="#3b3127"/><path d="M6,12 H18 M6,17 H18 M6,22 H14" stroke="#c99a3b" stroke-width="2"/></svg></div>
        <div><div class="service__label">Kostenlose</div><div class="service__text">Erstellung Ihres<br>Energieausweises</div></div>
      </div>
      <div class="service">
        <div class="service__icon"><svg width="32" height="30" viewBox="0 0 32 30" fill="#3b3127"><rect x="12" y="11" width="8" height="8"/><path d="M13,12 L6,6 M19,12 L26,6 M13,18 L6,24 M19,18 L26,24" stroke="#3b3127" stroke-width="2.5"/><circle cx="5" cy="5" r="4"/><circle cx="27" cy="5" r="4"/><circle cx="5" cy="25" r="4"/><circle cx="27" cy="25" r="4"/></svg></div>
        <div><div class="service__label">Kostenlose</div><div class="service__text">Drohnenaufnahmen<br>Ihrer Immobilien</div></div>
      </div>
    </div>
  </div>

  <div class="contact contact--address">
    <span class="contact__icon"><svg width="10" height="12" viewBox="0 0 10 12"><path d="M5,0 A5,5 0 0 1 10,5 Q10,8 5,12 Q0,8 0,5 A5,5 0 0 1 5,0 Z" fill="#fff"/></svg></span>
    <span><strong>Brenkholt &amp; Partner Bremen</strong><br>28209 Bremen-Lindenweg 14</span>
  </div>
  <div class="contact contact--phone">
    <span class="contact__icon"><svg width="10" height="10" viewBox="0 0 10 10"><path d="M1,1 L3.5,0.5 L4.5,3 L3,4 Q4,6 6,7 L7,5.5 L9.5,6.5 L9,9 Q4,9.5 1,1 Z" fill="#fff"/></svg></span>
    <span><strong>Telefon Bremen:</strong><br>+49(0) 421 555 0190</span>
  </div>
  <div class="contact-url">www.brenkholt-immobilien.de</div>
  <div class="contact contact--mail">
    <span class="contact__icon"><svg width="11" height="8" viewBox="0 0 11 8"><rect x=".5" y=".5" width="10" height="7" fill="none" stroke="#fff"/><path d="M.5,.5 L5.5,4.5 L10.5,.5" fill="none" stroke="#fff"/></svg></span>
    <span><strong>E-Mail:</strong><br>bremen@brenkholt-immobilien.de</span>
  </div>
</section>

<!-- Back side -->
<section class="flyer flyer--back">
  <div class="street" role="img" aria-label="Foto einer Altbaustraße mit Bäumen und parkenden Autos"></div>

  <div class="hotline">
    <div class="hotline__icon"><svg width="28" height="28" viewBox="0 0 10 10"><path d="M1,1 L3.5,0.5 L4.5,3 L3,4 Q4,6 6,7 L7,5.5 L9.5,6.5 L9,9 Q4,9.5 1,1 Z" fill="#fff"/></svg></div>
    <div class="hotline__text">
      <div class="hotline__label">kostenlose Rufnummer</div>
      <div class="hotline__number">+49800 0300 420</div>
    </div>
  </div>

  <svg class="layer" viewBox="0 0 820 1160" aria-hidden="true">
    <path d="M0,430 Q410,390 820,410 L820,560 Q410,600 0,560 Z" fill="#3b3127"/>
    <path d="M0,420 Q410,380 820,400" fill="none" stroke="#c99a3b" stroke-width="5"/>
    <path d="M0,570 Q410,610 820,570" fill="none" stroke="#c99a3b" stroke-width="5"/>
    <path d="M0,578 Q410,618 820,578 L820,1160 L0,1160 Z" fill="#ffffff"/>
    <path d="M0,960 C320,965 600,1010 820,1085" fill="none" stroke="#c99a3b" stroke-width="5"/>
    <path d="M0,975 C320,980 600,1025 820,1100 L820,1160 L0,1160 Z" fill="#3b3127"/>
  </svg>

  <div class="tip-title">
    <div class="tip-title__main">TIPPGEBERPRÄMIE</div>
    <div class="tip-title__sub">Brenkholt &amp; Partner Immobilien</div>
  </div>

  <div class="tip-body">
    <p><strong>So einfach</strong> verdienen Sie sich Ihre Tippprämie, wenn Sie Kenntnis vom beabsichtigten Verkauf einer Immobilie haben, dann setzen Sie sich mit uns in Verbindung.</p>
    <p>Wir belohnen Ihren Tipp – wenn er zu einem Verkaufsabschluss durch uns führt – mit 10 Prozent der an uns gezahlten Netto-Vermittlungsprovision (ohne MwSt.). Dies gilt auch für Eigentümer, die uns Ihre Immobilie zum Verkauf geben.</p>
    <p><strong>Voraussetzungen für die Zahlung einer Tippgeber-Prämie sind:</strong></p>
    <ul class="conditions">
      <li>Die Brenkholt &amp; Partner Immobilien kennt das angebotene Objekt noch nicht.</li>
      <li>Das Objekt wird nicht bereits im Internet von dritter Seite beworben.</li>
      <li>Die Brenkholt &amp; Partner Immobilien erhält die Erlaubnis zur Vermarktung der Immobilie.</li>
      <li>Es kommt zu einem durch die Brenkholt &amp; Partner Immobilien vermittelten Verkauf.</li>
      <li>Sie erhalten Ihre Tippprämie unmittelbar nach Zahlung der Courtage an uns auf ein von Ihnen genanntes Konto überwiesen!</li>
    </ul>
  </div>

  <div class="contact contact--address">
    <span class="contact__icon"><svg width="10" height="12" viewBox="0 0 10 12"><path d="M5,0 A5,5 0 0 1 10,5 Q10,8 5,12 Q0,8 0,5 A5,5 0 0 1 5,0 Z" fill="#fff"/></svg></span>
    <span><strong>Brenkholt &amp; Partner Bremen</strong><br>28209 Bremen-Lindenweg 14</span>
  </div>
  <div class="contact contact--phone">
    <span class="contact__icon"><svg width="10" height="10" viewBox="0 0 10 10"><path d="M1,1 L3.5,0.5 L4.5,3 L3,4 Q4,6 6,7 L7,5.5 L9.5,6.5 L9,9 Q4,9.5 1,1 Z" fill="#fff"/></svg></span>
    <span><strong>Telefon Bremen:</strong><br>+49(0) 421 555 0190</span>
  </div>
  <div class="contact-url">www.brenkholt-immobilien.de</div>
  <div class="contact contact--mail">
    <span class="contact__icon"><svg width="11" height="8" viewBox="0 0 11 8"><rect x=".5" y=".5" width="10" height="7" fill="none" stroke="#fff"/><path d="M.5,.5 L5.5,4.5 L10.5,.5" fill="none" stroke="#fff"/></svg></span>
    <span><strong>E-Mail:</strong><br>bremen@brenkholt-immobilien.de</span>
  </div>
</section>

</body>
</html>
```